Oregon Pawnbroker About Us Brochure

We need to make a front/back tri-fold "about us" informative brochure using the bullet points uploaded. Our association represents licensed pawnbrokers in the state of Oregon and this will be distributed to the entire legislative body in our state. I have attached our logo, but feel free to be creative with logo to enhance the overall appearance of the brochure.

Target Market(s)

Regulators and Politicians

Industry/Entity Type

Pawnbroker

Requirements
Must have
• Professional Appearance
Nice to have
• Graphics, color scheme

```html
<!DOCTYPE html>
<html lang="en">
<head>
<meta charset="utf-8">
<title>Oregon Pawnbrokers – About Our Industry</title>
<link href="https://fonts.googleapis.com/css2?family=Encode+Sans+Condensed:wght@300;400&display=swap" rel="stylesheet">
<style>
:root{
  --orange:#ff5014;
  --navy:#17263a;
  --ink:#2a2f38;
  --paper:#f1f1f1;
  --paper-dark:#d6d6d6;
  --white:#ffffff;
}
*{margin:0;padding:0;box-sizing:border-box}
html,body{width:1200px;height:848px;overflow:hidden;background:var(--white)}
body{font-family:"Encode Sans Condensed",sans-serif;font-weight:300;color:var(--ink)}
.brochure{position:relative;width:1200px;height:848px;overflow:hidden}
.panel{position:absolute;top:0;height:848px;width:400px;overflow:hidden}
.panel--about{left:0}
.panel--regulation{left:400px;background:linear-gradient(100deg,#c9c9c9 0%,#efefef 6%,#f3f3f3 60%,#e4e4e4 100%)}
.panel--why{left:800px;background:linear-gradient(100deg,#c4c4c4 0%,#e6e6e6 6%,#dedede 50%,#d0d0d0 100%)}
.facets{position:absolute;inset:0}
.band{position:absolute;left:0;bottom:0;width:400px;height:12px;background:var(--navy)}
.panel--regulation .band{background:var(--orange)}

/* About panel */
.office-photo{position:absolute;inset:0;background:linear-gradient(180deg,#6b7076 0%,#8a8e93 30%,#5a5e63 65%,#3b3e42 100%)}
.about-card{position:absolute;left:44px;top:130px;width:311px;height:588px;background:var(--orange);color:var(--white);padding:58px 29px 0 29px}
.about-card .fold{position:absolute;right:0;top:0}
.about-card h2{font-weight:300;line-height:1}
.about-card .kicker{display:block;font-size:20px;letter-spacing:.5px;color:var(--navy)}
.about-card .title{display:block;font-size:35px;margin-top:4px;letter-spacing:.3px}
.about-card p{font-size:12.3px;line-height:15.7px;text-align:justify;margin-top:15.5px}
.about-card p:first-of-type{margin-top:25px}
.about-card .em{color:var(--navy);font-weight:400}
.about-card .globe{position:absolute;left:257px;top:538px}

/* Regulation panel */
.regulation{position:absolute;left:53px;top:74px;width:295px}
.regulation h2{font-weight:300;font-size:35px;color:var(--orange);letter-spacing:.5px;line-height:1}
.regulation p{font-size:12.2px;line-height:15.7px;text-align:justify;margin-top:15.5px}
.regulation p:first-of-type{margin-top:25px}
.regulation .ref{color:var(--orange)}
.regulators{list-style:none;text-align:center;font-size:14.6px;line-height:18.5px;margin-top:20px;color:var(--navy);font-weight:400}
.divider{position:absolute;left:100px;top:482px;width:198px;border-top:1px dashed var(--navy)}
.chart-icon{position:absolute;left:314px;top:482px}
.stats-head{position:absolute;left:0;top:533px;width:400px;text-align:center;line-height:1}
.stats-head .kicker{display:block;font-size:20px;letter-spacing:1px;color:var(--navy)}
.stats-head .title{display:block;font-size:35px;color:var(--orange);margin-top:6px}
.stats-head .source{display:block;font-size:12px;font-style:italic;margin-top:6px;color:#555}
.stats{position:absolute;left:53px;top:638px;width:295px;list-style:none;font-size:15.5px;line-height:20px;color:var(--navy);text-align:center}
.stats li{margin-bottom:2px}
.stats li::before{content:"• ";font-size:12px}
.stats .hl{color:var(--orange)}

/* Why panel */
.hands-photo{position:absolute;left:0;top:144px;width:346px;height:137px;background:radial-gradient(ellipse at 55% 45%,#b07a3a 0%,#6a4a3a 35%,#3b3844 70%,#2c2f38 100%)}
.why-head{position:absolute;left:56px;top:322px;line-height:1}
.why-head .line{display:block;font-size:35px;color:var(--navy);letter-spacing:.3px}
.why-head .accent{color:var(--orange)}
.why-head .sub{display:block;font-size:19px;letter-spacing:1.5px;color:var(--orange);margin-top:3px}
.bulb{position:absolute;left:314px;top:387px}
.why-body{position:absolute;left:50px;top:458px;width:294px}
.why-body p{font-size:12.2px;line-height:15.7px;text-align:justify;margin-bottom:15.5px}
.handshake{position:absolute;left:186px;top:717px}
.site{position:absolute;left:0;top:790px;width:400px;text-align:center;font-size:12px;color:var(--navy);font-weight:400}
</style>
</head>
<body>
<main class="brochure">

  <section class="panel panel--about">
    <div class="office-photo" role="img" aria-label="Monochrome photo of an open-plan office with exposed ceiling ducts and a person working at a desk"></div>
    <article class="about-card">
      <svg class="fold" width="125" height="38" viewBox="0 0 125 38"><polygon points="0,0 125,0 125,20 55,38" fill="#ffffff"/><polygon points="0,0 55,38 40,38" fill="#e0e0e0"/></svg>
      <h2><span class="kicker">ABOUT</span><span class="title">OUR INDUSTRY</span></h2>
      <p>Pawnbroking is the oldest form of regulated consumer credit.</p>
      <p>The Department of Consumer and Business Services issues the pawnbroker licenses here in Oregon.</p>
      <p>Currently, Oregon has 83 individually licensed pawnshops, 78 of which are brick-and-mortar, family-owned and operated businesses.</p>
      <p>Pawnbrokers offer highly regulated safety-net funds to consumers on a face-to-face basis from Main Street locations across the state.</p>
      <p>Lending decisions are solely based on the collateral and pawn transactions are non-recourse. <span class="em">No credit inquiries, No credit reporting, No collections, No cycle of debt.</span></p>
      <p>Pawnbrokers provide safe, secure storage for items customers cannot or do not want to store themselves, including oversized or seasonal items construction equipment, and firearms.</p>
      <svg class="globe" width="22" height="22" viewBox="0 0 22 22" fill="none" stroke="#fff" stroke-width="1.4"><circle cx="11" cy="11" r="9.5"/><ellipse cx="11" cy="11" rx="4" ry="9.5"/><line x1="1.5" y1="11" x2="20.5" y2="11"/><line x1="3" y1="6" x2="19" y2="6"/><line x1="3" y1="16" x2="19" y2="16"/></svg>
    </article>
    <div class="band"></div>
  </section>

  <section class="panel panel--regulation">
    <svg class="facets" width="400" height="848" viewBox="0 0 400 848"><polygon points="60,0 400,0 400,380 180,848 120,848" fill="#ffffff" opacity=".35"/><polygon points="400,380 400,848 180,848" fill="#d8d8d8" opacity=".4"/></svg>
    <div class="regulation">
      <h2>REGULATION</h2>
      <p>Pawnshops are heavily regulated and work closely with the federal, stateand local governments and law enforcement.</p>
      <p><span class="ref">ORS 726</span> and <span class="ref">OAR 441-740</span> define the requirements for our industry here in Oregon including the requirements of a loan, duration of a loan, as well as the interest and fees charged.</p>
      <p>Transactions require customer to present government issued photo identification.</p>
      <p>All transactions are reported daily to law enforcement.</p>
      <p style="text-align:left">Oregon Pawnbrokers work closely with the following regulators:</p>
      <ul class="regulators">
        <li>Department of Consumer &amp; Business Services</li>
        <li>Bureau of Alcohol Tobacco &amp; Firearms</li>
        <li>State Police</li>
        <li>Department of Agriculture</li>
      </ul>
    </div>
    <div class="divider"></div>
    <svg class="chart-icon" width="26" height="28" viewBox="0 0 26 28" fill="none" stroke="#17263a" stroke-width="1.4"><rect x="2" y="3" width="22" height="16"/><line x1="1" y1="3" x2="25" y2="3"/><rect x="6" y="11" width="3" height="5"/><rect x="11.5" y="8" width="3" height="8"/><rect x="17" y="10" width="3" height="6"/><line x1="13" y1="19" x2="13" y2="24"/><line x1="9" y1="27" x2="13" y2="24"/><line x1="17" y1="27" x2="13" y2="24"/></svg>
    <div class="stats-head">
      <span class="kicker">OREGON PAWNBROKER</span>
      <span class="title">STATISTICS</span>
      <span class="source">(as reported bt DCBS)</span>
    </div>
    <ul class="stats">
      <li>Average loan amount in 2020 was $175</li>
      <li>Redemption rate of 72%</li>
      <li class="hl">Oregon pawnshops made approximately 206,500 loans in 2020, lending $33.2 million to Oregon customers.</li>
      <li>Police pickup rate of 0.085%</li>
    </ul>
    <div class="band"></div>
  </section>

  <section class="panel panel--why">
    <svg class="facets" width="400" height="848" viewBox="0 0 400 848"><polygon points="103,0 400,0 400,50 210,88" fill="#ffffff"/><polygon points="103,0 210,88 190,85" fill="#e2e2e2"/><polygon points="90,120 400,260 400,848 300,848" fill="#ffffff" opacity=".25"/></svg>
    <div class="hands-photo" role="img" aria-label="Photo of cupped hands holding a glowing string of warm lights"></div>
    <h2 class="why-head">
      <span class="line"><span class="accent">WHY</span> PAWNBROKERS</span>
      <span class="line">ARE IMPORTANT</span>
      <span class="sub">TO OREGON CONSUMERS</span>
    </h2>
    <svg class="bulb" width="18" height="28" viewBox="0 0 18 28" fill="none" stroke="#ff5014" stroke-width="1.4"><path d="M9 1a8 8 0 0 0-5 14c1 1 1.5 2 1.5 4h7c0-2 .5-3 1.5-4A8 8 0 0 0 9 1z"/><line x1="5.5" y1="22" x2="12.5" y2="22"/><line x1="6.5" y1="25" x2="11.5" y2="25"/></svg>
    <div class="why-body">
      <p>Without state-licensed pawnbrokers, Oregonians could be forced to borrow from unlicensed people with unregulated loans that include very high interest rates or instead, forced to sell their property entirely, diminishing their personal assets.</p>
      <p>Other credit based lenders, such as banks and credit unions, do not offer Oregonians loan products at the small dollar amounts our industry serves.</p>
      <p>Pawnbrokers provide a same day financial solution.</p>
      <p>Pawnbrokers are invested in our communities and are sensitive to the needs of our customers.</p>
    </div>
    <svg class="handshake" width="32" height="26" viewBox="0 0 32 26" fill="none" stroke="#17263a" stroke-width="1.5" stroke-linejoin="round"><path d="M1 9l7-7 5 3 5-3 7 7-12 13z"/><path d="M13 5l-5 5 3 2 4-4"/><path d="M11 15l3 3M14 13l3 3M17 11l3 3"/></svg>
    <div class="site">www.cascadepawnguild.org</div>
    <div class="band"></div>
  </section>

</main>
</body>
</html>
```